Interior Design & consultancy firm requires a new business card design that is a little bit funky bu

Meridale Design Services is a leading strategic design practice specialising in the development and implementation of strategies and design solutions for commercial workplaces across a wide variety of industries.

The company has over twenty years experience in the strategic design, development and construction of innovative and efficient workplace environments for the commercial, corporate and industrial sectors.

We believe good design and efficient workspaces can transform companies, improve people’s lives and increase productivity.

Target Market(s)

My clients are mainly Government or corporate clients wanting to create a statement with their office fitout & new furniture that reflects their corporate identity

Industry/Entity Type

Construction

Font styles to use
Sans Serif

Colors
add136

Requirements
Must have
• The business card must be easy to read, simple & highlight my name & mobile phone number
Should not have
• I do not want the card to be fussy, feature too many colours or look to busy.

```html
<!DOCTYPE html>
<html lang="en">
<head>
<meta charset="utf-8">
<title>Meridale Design Services – Business Card</title>
<link rel="stylesheet" href="https://fonts.googleapis.com/css2?family=Jost:wght@300;400;500&display=swap">
<style>
  :root {
    --backdrop: #e4fc98;
    --card-green: #add136;
    --card-text: #ffffff;
    --card-ink: #1a1a1a;
  }
  * { margin: 0; padding: 0; box-sizing: border-box; }
  html, body {
    width: 1200px;
    height: 900px;
    overflow: hidden;
    background: var(--backdrop);
  }
  .stage {
    position: relative;
    width: 1200px;
    height: 900px;
    font-family: "Jost", "Century Gothic", sans-serif;
  }
  .card {
    position: absolute;
    top: 307px;
    width: 500px;
    height: 286px;
    border-radius: 16px;
    background: var(--card-green);
    color: var(--card-text);
    overflow: hidden;
  }
  .card--front { left: 70px; }
  .card--back  { left: 630px; }

  /* Front */
  .front-wordmark {
    position: absolute;
    left: 0; right: 0;
    top: 78px;
    text-align: center;
    font-weight: 300;
    font-size: 58px;
    letter-spacing: 1px;
    line-height: 1;
  }
  .front-company {
    position: absolute;
    left: 0; right: 0;
    top: 168px;
    text-align: center;
    font-weight: 300;
    font-size: 25px;
    letter-spacing: 0.3px;
  }

  /* Back */
  .back-wordmark {
    position: absolute;
    right: 34px;
    top: 30px;
    font-weight: 300;
    font-size: 40px;
    line-height: 1;
  }
  .contact {
    position: absolute;
    left: 36px;
    top: 104px;
  }
  .contact-name {
    font-weight: 400;
    font-size: 30px;
    letter-spacing: 0.8px;
    line-height: 1.1;
  }
  .contact-role {
    margin-top: 8px;
    font-weight: 500;
    font-size: 15px;
    color: var(--card-ink);
    letter-spacing: 0.3px;
  }
  .contact-role .divider { padding: 0 3px; font-weight: 300; }
  .contact-phone {
    margin-top: 12px;
    font-weight: 400;
    font-size: 38px;
    letter-spacing: 2px;
    line-height: 1;
  }
</style>
</head>
<body>
  <main class="stage">
    <section class="card card--front" aria-label="Business card front">
      <p class="front-wordmark">Meridale</p>
      <p class="front-company">Meridale Design Services Pty. Ltd.</p>
    </section>

    <section class="card card--back" aria-label="Business card back">
      <p class="back-wordmark">Meridale</p>
      <div class="contact">
        <p class="contact-name">Carla Whitmore</p>
        <p class="contact-role">Director<span class="divider">|</span>Senior Interior Designer</p>
        <p class="contact-phone">0400 512 873</p>
      </div>
    </section>
  </main>
</body>
</html>
```